Geschäftspapiere für industriellen 3D-Druck
Zielgruppe
Industrieller 3D Druck
Aufgabenstellung
Industrielles, zukunftorientieres Design, ähnliche Farben wie das Logo
In der unteren Briefkopfzeile sollen die Adresse, sowie die Bankdaten aufgeführt werden. In der oberen Briefkopfzeile ebenfalls die Adresse des Unternehmens, sowie das Unternehmenslogo.

```html
<!DOCTYPE html>
<html lang="de">
<head>
<meta charset="utf-8">
<title>KORVANTIS – Geschäftspapiere</title>
<link rel="stylesheet" href="https://fonts.googleapis.com/css2?family=Jost:wght@400;500;600&display=swap">
<style>
  :root{
    --page:#ffffff;
    --ink:#1a1a1a;
    --ink-soft:#333333;
    --brand:#0f5d9e;
    --brand-light:#1f7ab8;
    --brand-dark:#0a4a86;
    --night:#000000;
    --steel:#3a3a3a;
    --logo-dim:#5a5a5a;
    --shade:rgba(0,0,0,.45);
  }
  *{margin:0;padding:0;box-sizing:border-box}
  html,body{width:1200px;height:1200px;overflow:hidden;background:var(--page)}
  body{position:relative;font-family:"Jost",sans-serif;color:var(--ink)}

  .letter{position:absolute;left:292px;top:87px;width:624px;height:838px;background:var(--page);box-shadow:5px 5px 7px var(--shade)}
  .brand{position:absolute;display:flex;align-items:center;gap:7px;font-family:"Jost",sans-serif;font-weight:600;letter-spacing:.06em;line-height:1}
  .brand-mark{display:block;background:var(--brand)}
  .letter .brand{left:394px;top:40px}
  .letter .brand-mark{width:26px;height:26px}
  .letter .brand-name{font-size:23px;color:var(--ink-soft)}

  .sender-block{position:absolute;left:31px;top:225px;font-size:9px;line-height:12px;color:var(--ink)}
  .sender-block .sender-name{font-weight:600;color:var(--ink-soft)}
  .salutation{position:absolute;left:31px;top:357px;font-size:19px;font-weight:400}
  .body-copy{position:absolute;left:31px;width:569px;font-size:6.1px;line-height:8.5px;color:var(--ink)}
  .body-copy p{margin:0}
  .signature{position:absolute;left:458px;top:666px;width:136px;height:70px;background:linear-gradient(135deg,#f4f4f4,#e6e6e6);border-radius:3px}

  .letter-footer{position:absolute;left:0;top:773px;width:100%;font-size:11.3px;line-height:15px;color:var(--ink)}
  .footer-col{position:absolute;top:0}
  .footer-address{left:33px}
  .footer-contact{left:222px}
  .footer-bank{left:381px;width:240px}
  .footer-divider{position:absolute;top:2px;width:1px;height:40px;background:var(--ink)}
  .bank-row{display:flex;white-space:nowrap}
  .bank-row .label{width:65px}
  .contact-row{display:flex;align-items:center;gap:5px;white-space:nowrap}
  .icon{flex:none;display:block}
  .letter-band{position:absolute;left:0;bottom:0;width:100%;height:11px;background:linear-gradient(90deg,var(--brand-light),var(--brand-dark))}

  .card{position:absolute;top:956px;width:309px;height:164px;box-shadow:5px 5px 7px var(--shade)}
  .card-back{left:291px;background:var(--night)}
  .card-front{left:608px;background:var(--page)}
  .card .brand{left:50%;top:68px;transform:translateX(-50%)}
  .card .brand-mark{width:22px;height:22px}
  .card .brand-name{font-size:17px}
  .card-back .brand-mark{background:var(--brand-dark)}
  .card-back .brand-name{color:var(--logo-dim)}
  .card-front .brand-name{color:var(--ink-soft)}
  .card-details{position:absolute;top:125px;font-size:8px;line-height:10.5px;color:var(--ink)}
  .card-details.left{left:19px}
  .card-details.right{left:193px}
  .card-details .contact-row{gap:4px}
  .card-band-dark{position:absolute;left:0;top:160px;width:66px;height:4px;background:var(--steel)}
  .card-band-blue{position:absolute;left:69px;top:160px;width:240px;height:4px;background:linear-gradient(90deg,var(--brand-light),var(--brand-dark))}
</style>
</head>
<body>

<svg width="0" height="0" style="position:absolute" aria-hidden="true">
  <symbol id="ic-phone" viewBox="0 0 20 20"><circle cx="10" cy="10" r="10" fill="#0f5d9e"/><path d="M6.5 5.5l2 0 1 2.5-1.3 1c.7 1.4 1.6 2.3 3 3l1-1.3 2.5 1v2c0 .6-.5 1-1 1C9.3 14.7 5.3 10.7 5.5 6.5c0-.6.4-1 1-1z" fill="#fff"/></symbol>
  <symbol id="ic-mail" viewBox="0 0 20 20"><circle cx="10" cy="10" r="10" fill="#0f5d9e"/><rect x="5" y="6.5" width="10" height="7" rx="1.5" fill="#fff"/></symbol>
  <symbol id="ic-web" viewBox="0 0 20 20"><circle cx="10" cy="10" r="10" fill="#0f5d9e"/><circle cx="10" cy="10" r="5" fill="none" stroke="#fff" stroke-width="1.4"/><path d="M5 10h10M10 5c-2.5 3-2.5 7 0 10M10 5c2.5 3 2.5 7 0 10" fill="none" stroke="#fff" stroke-width="1"/></symbol>
</svg>

<section class="letter" aria-label="Briefbogen">
  <div class="brand"><span class="brand-mark"></span><span class="brand-name">KORVANTIS</span></div>

  <div class="sender-block">
    <div><span class="sender-name">KORVANTIS</span> / Street name here / Your city here</div>
    <div>Recipient Name</div>
    <div>Organization Name</div>
    <div>Street address</div>
    <div>City - Zip code</div>
  </div>

  <h1 class="salutation">Dear Name Here,</h1>

  <div class="body-copy" style="top:430px">
    <p>Thank you for your interest in our industrial additive manufacturing services. We produce functional prototypes, small series and spare parts from metal and polymer powders on modern laser sintering systems. Every order is checked by our engineers for printability, tolerances and surface quality before production starts, and we document materials, build parameters and inspection results for each part we deliver to you. Our team is happy to advise you on design and finishing.</p>
    <p>Please send us your CAD data and requirements, and we will prepare a detailed quotation with delivery dates within two working days. For urgent projects we also offer express production and direct shipping.</p>
  </div>
  <div class="body-copy" style="top:481px">
    <p>Thank you for your interest in our industrial additive manufacturing services. We produce functional prototypes, small series and spare parts from metal and polymer powders on modern laser sintering systems. Every order is checked by our engineers for printability, tolerances and surface quality before production starts, and we document materials, build parameters and inspection results for each part we deliver to you. Our team is happy to advise you on design and finishing.</p>
    <p>Please send us your CAD data and requirements, and we will prepare a detailed quotation with delivery dates within two working days. For urgent projects we also offer express production and direct shipping.</p>
  </div>
  <div class="body-copy" style="top:541px">
    <p>Thank you for your interest in our industrial additive manufacturing services. We produce functional prototypes, small series and spare parts from metal and polymer powders on modern laser sintering systems. Every order is checked by our engineers for printability, tolerances and surface quality before production starts, and we document materials, build parameters and inspection results for each part we deliver to you. Our team is happy to advise you on design and finishing.</p>
    <p>Please send us your CAD data and requirements, and we will prepare a detailed quotation with delivery dates within two working days. For urgent projects we also offer express production and direct shipping.</p>
  </div>
  <div class="body-copy" style="top:600px">
    <p>Thank you for your interest in our industrial additive manufacturing services. We produce functional prototypes, small series and spare parts from metal and polymer powders on modern laser sintering systems. Every order is checked by our engineers for printability, tolerances and surface quality before production starts, and we document materials, build parameters and inspection results for each part we deliver to you. Our team is happy to advise you on design and finishing.</p>
  </div>

  <div class="signature" role="img" aria-label="Handschriftliche Unterschrift"></div>

  <footer class="letter-footer">
    <div class="footer-col footer-address">
      <div>YOUR NAME</div><div>adress here</div><div>0000 city</div>
    </div>
    <span class="footer-divider" style="left:161px"></span>
    <div class="footer-col footer-contact">
      <div class="contact-row"><svg class="icon" width="10" height="10"><use href="#ic-phone"/></svg>+49 (0)000 0000</div>
      <div class="contact-row"><svg class="icon" width="10" height="10"><use href="#ic-mail"/></svg>info@YOUR NAME.de</div>
      <div class="contact-row"><svg class="icon" width="10" height="10"><use href="#ic-web"/></svg>www.YOUR NAME.de</div>
    </div>
    <span class="footer-divider" style="left:363px"></span>
    <div class="footer-col footer-bank">
      <div class="bank-row">Banknerbindung xxxxxxxxxxxxxxxxxxxxxx</div>
      <div class="bank-row"><span class="label">IBAN</span>DE000000000000000000000</div>
      <div class="bank-row"><span class="label">BIC</span>XXXXXXXXXX</div>
    </div>
  </footer>
  <div class="letter-band"></div>
</section>

<section class="card card-back" aria-label="Visitenkarte Rückseite">
  <div class="brand"><span class="brand-mark"></span><span class="brand-name">KORVANTIS</span></div>
</section>

<section class="card card-front" aria-label="Visitenkarte Vorderseite">
  <div class="brand"><span class="brand-mark"></span><span class="brand-name">KORVANTIS</span></div>
  <div class="card-details left">
    <div>YOUR NAME</div><div>adress here</div><div>0000 city</div>
  </div>
  <div class="card-details right">
    <div class="contact-row"><svg class="icon" width="7" height="7"><use href="#ic-phone"/></svg>+49 (0)000 0000</div>
    <div class="contact-row"><svg class="icon" width="7" height="7"><use href="#ic-mail"/></svg>info@YOUR NAME.de</div>
    <div class="contact-row"><svg class="icon" width="7" height="7"><use href="#ic-web"/></svg>www.YOUR NAME.de</div>
  </div>
  <span class="card-band-dark"></span>
  <span class="card-band-blue"></span>
</section>

</body>
</html>
```